Flyer / Mailer for Business Debt Relief Business - Harborline Relief 6" x 11"

We need a 6" x 11" double sided flyer. This will be sent out to potential customers with high interest business loans. We would like the design to coordinate with the colors of our logo. I have included a mock up that we sketched out. I have also included a file of a mailer we received that we would like to use as a template (not colors or fonts, just set up). I have also included an .ai file of our logo.

```html
<!DOCTYPE html>
<html lang="en">
<head>
<meta charset="utf-8">
<title>Harborline Relief – Mailer</title>
<link rel="stylesheet" href="https://fonts.googleapis.com/css2?family=Questrial&family=Noto+Serif:ital,wght@0,400;1,400;1,700&display=swap">
<style>
  :root {
    --stage: #767676;
    --paper: #ffffff;
    --blue: #0a6ab0;
    --green: #4fae2f;
    --ink: #1c1c1c;
    --grey-text: #8a8a8a;
    --sky-top: #e4f4fb;
    --sky-bottom: #f6fbfe;
  }
  * { box-sizing: border-box; margin: 0; padding: 0; }
  html, body { width: 1200px; height: 1200px; overflow: hidden; background: var(--stage); }
  body { position: relative; font-family: "Noto Serif", serif; color: var(--ink); }

  .card { position: absolute; left: 160px; width: 880px; height: 480px; background: var(--paper); overflow: hidden; }
  .card--front { top: 66px; }
  .card--back { top: 653px; }

  /* front */
  .photo { position: absolute; left: 0; width: 240px; }
  .photo--savings { top: 0; height: 158px; background: linear-gradient(135deg, #b9a9d8, #f2eef4 60%, #f3b8c4); }
  .photo--coins { top: 161px; height: 157px; background: radial-gradient(circle at 45% 55%, #b8a47a, #ece9e2 60%, #f6f6f6); }
  .photo--seedling { top: 321px; height: 159px; background: linear-gradient(135deg, #8c7659, #d9b79c 50%, #6e5a43); }

  .message { position: absolute; left: 240px; top: 0; width: 640px; height: 480px;
    background: linear-gradient(180deg, var(--sky-top), var(--sky-bottom) 70%); }
  .tagline { position: absolute; left: 30px; top: 26px; font-family: "Questrial", sans-serif; font-weight: 400; font-size: 23px; color: #222; white-space: nowrap; }
  .front-brand { position: absolute; right: 10px; top: 56px; display: flex; align-items: center; gap: 6px;
    font-family: "Questrial", sans-serif; font-size: 13px; color: #333; }
  .front-brand .mark { width: 12px; height: 12px; background: var(--green); }
  .brand-rule { position: absolute; right: 0; top: 81px; width: 160px; height: 2px; background: var(--green); }
  .intro-band { position: absolute; left: 0; top: 66px; width: 640px; height: 59px; background: var(--blue);
    clip-path: polygon(0 0, 475px 0, 495px 18px, 100% 18px, 100% 100%, 0 100%); }
  .intro-band p { position: absolute; left: 24px; top: 8px; width: 470px; color: #fff; font-style: italic; font-weight: 700; font-size: 15px; line-height: 22px; }
  .question { position: absolute; left: 24px; top: 134px; color: var(--blue); font-style: italic; font-weight: 700; font-size: 18px; white-space: nowrap; }
  .shout { position: absolute; left: 24px; top: 158px; color: var(--green); font-style: italic; font-weight: 700; font-size: 25px; }
  .benefits { position: absolute; left: 24px; top: 198px; list-style: none; font-size: 14px; line-height: 20.4px; white-space: nowrap; }
  .benefits li::before { content: "•"; color: var(--blue); margin-right: 5px; }
  .contact-band { position: absolute; left: 0; bottom: 0; width: 640px; height: 91px; background: var(--green); color: #fff; }
  .contact-band p { position: absolute; left: 20px; width: 352px; text-align: center; white-space: nowrap; line-height: 1; }
  .contact-band .site { top: 10px; font-size: 14px; }
  .contact-band .site em { font-weight: 700; }
  .contact-band .call { top: 31px; font-size: 10px; }
  .contact-band .phone { top: 46px; font-size: 20px; }
  .contact-band .mail { top: 72px; font-size: 14px; }
  .photo--advisor { position: absolute; left: 648px; top: 150px; width: 232px; height: 330px;
    background: linear-gradient(180deg, #c9a88d 0%, #1d2b4a 45%, #16213a 100%); border-radius: 110px 110px 0 0; }

  /* back */
  .back-brand { position: absolute; left: 67px; top: 60px; }
  .back-brand .mark { width: 52px; height: 52px; background: var(--green); margin: 0 0 12px 60px; }
  .back-brand .name { font-family: "Questrial", sans-serif; font-size: 16px; color: #333; }
  .address { position: absolute; left: 67px; top: 164px; font-family: "Questrial", sans-serif; font-size: 11px; line-height: 14px; color: var(--grey-text); }
  .back-headline { position: absolute; left: 67px; top: 238px; color: var(--blue); font-style: italic; font-weight: 700; font-size: 22px; line-height: 34px; white-space: nowrap; }
  .back-copy { position: absolute; left: 68px; top: 329px; font-style: italic; font-weight: 700; font-size: 15.5px; line-height: 24.3px; white-space: nowrap; }
  .divider { position: absolute; left: 440px; top: 36px; width: 2px; height: 410px; background: #6aa3cf; }
  .stamp-box { position: absolute; left: 767px; top: 42px; width: 65px; height: 77px; border: 1px solid #aaa; }
</style>
</head>
<body>
  <section class="card card--front">
    <div class="photo photo--savings" role="img" aria-label="Hand dropping a coin into a pink piggy bank"></div>
    <div class="photo photo--coins" role="img" aria-label="Burlap sack spilling gold coins"></div>
    <div class="photo photo--seedling" role="img" aria-label="Cupped hands holding soil with a young seedling"></div>

    <div class="message">
      <h1 class="tagline">Helping Business Focus On What Metters!</h1>
      <div class="front-brand"><span class="mark"></span>Harborline Relief</div>
      <div class="brand-rule"></div>
      <div class="intro-band"><p>We understand that merchant cash advance loans can be a burden on your business</p></div>
      <p class="question">Over whelmed by daily / weekly payments?</p>
      <p class="shout">WE CAN HELP!</p>
      <ul class="benefits">
        <li>This is not loan, WE ARE NOT LENDERS!</li>
        <li>Improve your business’s cash flow immediately</li>
        <li>Move payments to one monthly amount</li>
        <li>Reduce the amount you are pay’s out monthly</li>
        <li>Strategic alternatives to his interest loans</li>
        <li>Fast, Confidential business debt relief</li>
        <li>No-obliseton consultation</li>
        <li>Absolutely no credit polls</li>
        <li>No collateral, no financials</li>
      </ul>
      <div class="contact-band">
        <p class="site">Visit our website <em>www.harborlinerelief.com</em></p>
        <p class="call">Call now for free consultation with our Experts</p>
        <p class="phone">555-214-7730</p>
        <p class="mail">E-mail: info@harborlinerelief.com</p>
      </div>
    </div>
    <div class="photo--advisor" role="img" aria-label="Smiling businessman in a navy blazer, hand on chin, looking up thoughtfully"></div>
  </section>

  <section class="card card--back">
    <div class="back-brand">
      <div class="mark"></div>
      <p class="name">Harborline Relief</p>
    </div>
    <p class="address">410 Tidewater Ave<br>Marlow, Bexar County<br>78010 - USA</p>
    <h2 class="back-headline">Stvetesic Debit relief for<br>Businesses of All Sizes</h2>
    <p class="back-copy">Stop takins out loans to<br>pay off other loans.<br>Take back your business's<br>cash flow, and focus on<br>that matters.</p>
    <div class="divider"></div>
    <div class="stamp-box"></div>
  </section>
</body>
</html>
```